3 out of 100 people will get deadly skin cancer - we need a great illustration that shows this!

We put together a prototype image that communicates lifetime skin cancer risk. (see attached). We are looking for illustrators who can take make a new/better/cooler graphic that communicates this idea. It could be as simple as a superior illustration of the graphic we have or illustrators can propose a completely different idea.What should the illustration communicate?U.S. adults have a lifetime risk of developing skin cancer of 1 in 5. But we don't want to show 1 in 5; we want to show that number in a larger group. For example, in the attached illustration we show 20 in 100 people get skin cancer (i.e., 100 beach towels/umbrellas and 20 of them are red). Research has shown that people are more likely to accurately understand numbers like this when you convey them for larger groups (i.e., 20 out of 100 rather than 1 out of 5). U.S. adults also have a lifetime risk of 2.3% of developing the deadliest form of skin cancer (melanoma). In other words, approximately 3 in 100 people will develop melanoma in their lifetime. Ideally, a single image will convey both lifetime skin cancer risk (20 in 100) and melanoma risk (3 in 100). We will award a top three as follows: 1st place = $300, 2nd place = $250, third place = $200. We will also buy any design beyond 3rd place that we like for $100. For example, we purchased 24 designs in our last contest on Artquilla.This research is supported by funding from the University of Brenmoor.

Target Market(s)

The U.S. public; individuals at high risk of developing skin cancer

Industry/Entity Type

Medicine

Colors

Designer to choose colors to be used in the design.

Requirements
Must have
• an original illustration that conveys both lifetime risk of developing skin cancer (20 in 100) and melanoma (3 in 100).
Nice to have
• It can be beach towels and umbrellas, just like our prototype, or the designers can pitch an original idea. Imagery can be realistic or cartoonish (or something in between). It should be illustrations, though. Not edited photos. The image should be in color (no black and white illustrations).
Should not have
• Photos. Clip art. Free vector images.
• We are looking for original illustrations created by the designer.

```html
<!DOCTYPE html>
<html lang="en">
<head>
<meta charset="utf-8">
<title>How likely are you to get skin cancer?</title>
<link rel="stylesheet" href="https://fonts.googleapis.com/css2?family=Montserrat:wght@400;500;600&display=swap">
<style>
  :root {
    --sand: #fce8ab;
    --sea: #16a4e6;
    --sea-deep: #0f96d6;
    --clear: #1fb3e0;
    --cancer: #e8163c;
    --melanoma: #f7931e;
    --ink: #222222;
    --card: #ffffff;
  }
  * { box-sizing: border-box; margin: 0; padding: 0; }
  html, body { width: 1200px; height: 849px; overflow: hidden; }
  body {
    position: relative;
    background: var(--sand);
    font-family: "Montserrat", sans-serif;
    color: var(--ink);
  }
  .headline {
    position: absolute;
    top: 22px;
    left: 0;
    width: 100%;
    text-align: center;
    color: var(--sea);
    font-weight: 500;
    font-size: 43px;
    line-height: 58px;
    letter-spacing: 0.5px;
  }
  .headline .count { color: var(--cancer); font-weight: 600; }
  .questions {
    position: absolute;
    top: 134px;
    left: 0;
    width: 100%;
    text-align: center;
    font-size: 18px;
    line-height: 26px;
  }
  .crowd {
    position: absolute;
    top: 204px;
    left: 0;
    width: 100%;
  }
  .crowd-row {
    display: flex;
    justify-content: center;
    gap: 28px;
    height: 64px;
    align-items: center;
  }
  .towel {
    display: block;
    width: 52px;
    height: 22px;
    transform: skewX(-35deg);
    border-radius: 2px;
  }
  .towel--clear { background: var(--clear); }
  .towel--cancer { background: var(--cancer); }
  .towel--melanoma { background: var(--melanoma); }
  .shore {
    position: absolute;
    left: 0;
    bottom: 0;
    width: 1200px;
    height: 120px;
  }
  .legend {
    position: absolute;
    left: 17px;
    top: 695px;
    width: 128px;
    height: 137px;
    background: var(--card);
    border-radius: 10px;
    padding: 18px 10px;
    display: flex;
    flex-direction: column;
    justify-content: space-between;
  }
  .legend-item {
    display: flex;
    align-items: center;
    gap: 12px;
    font-size: 11px;
  }
  .legend-item .towel { width: 28px; height: 12px; margin-left: 4px; }
</style>
</head>
<body>
  <h1 class="headline">How likely are you to get skin cancer?<br>Let’s say <span class="count">100</span> people go to the beach…</h1>
  <p class="questions">How many will develop skin cancer in their lifetime?<br>How many will develop Melanoma, the deadliest form of skin cancer?</p>

  <div class="crowd" role="img" aria-label="100 beach towels: 77 without skin cancer, 20 with skin cancer, 3 with melanoma">
    <div class="crowd-row">
      <i class="towel towel--clear"></i><i class="towel towel--clear"></i><i class="towel towel--cancer"></i><i class="towel towel--clear"></i><i class="towel towel--clear"></i><i class="towel towel--clear"></i><i class="towel towel--cancer"></i><i class="towel towel--clear"></i><i class="towel towel--clear"></i><i class="towel towel--clear"></i><i class="towel towel--clear"></i><i class="towel towel--clear"></i><i class="towel towel--clear"></i>
    </div>
    <div class="crowd-row">
      <i class="towel towel--cancer"></i><i class="towel towel--clear"></i><i class="towel towel--clear"></i><i class="towel towel--cancer"></i><i class="towel towel--clear"></i><i class="towel towel--clear"></i><i class="towel towel--clear"></i><i class="towel towel--clear"></i><i class="towel towel--clear"></i><i class="towel towel--cancer"></i><i class="towel towel--clear"></i><i class="towel towel--clear"></i>
    </div>
    <div class="crowd-row">
      <i class="towel towel--cancer"></i><i class="towel towel--clear"></i><i class="towel towel--clear"></i><i class="towel towel--clear"></i><i class="towel towel--clear"></i><i class="towel towel--clear"></i><i class="towel towel--cancer"></i><i class="towel towel--clear"></i><i class="towel towel--clear"></i><i class="towel towel--clear"></i><i class="towel towel--clear"></i><i class="towel towel--clear"></i><i class="towel towel--cancer"></i>
    </div>
    <div class="crowd-row">
      <i class="towel towel--melanoma"></i><i class="towel towel--clear"></i><i class="towel towel--clear"></i><i class="towel towel--cancer"></i><i class="towel towel--clear"></i><i class="towel towel--clear"></i><i class="towel towel--cancer"></i><i class="towel towel--clear"></i><i class="towel towel--clear"></i><i class="towel towel--melanoma"></i><i class="towel towel--clear"></i><i class="towel towel--clear"></i>
    </div>
    <div class="crowd-row">
      <i class="towel towel--clear"></i><i class="towel towel--cancer"></i><i class="towel towel--clear"></i><i class="towel towel--clear"></i><i class="towel towel--clear"></i><i class="towel towel--clear"></i><i class="towel towel--clear"></i><i class="towel towel--clear"></i><i class="towel towel--clear"></i><i class="towel towel--clear"></i><i class="towel towel--clear"></i><i class="towel towel--cancer"></i><i class="towel towel--clear"></i>
    </div>
    <div class="crowd-row">
      <i class="towel towel--clear"></i><i class="towel towel--clear"></i><i class="towel towel--cancer"></i><i class="towel towel--clear"></i><i class="towel towel--clear"></i><i class="towel towel--cancer"></i><i class="towel towel--clear"></i><i class="towel towel--clear"></i><i class="towel towel--cancer"></i><i class="towel towel--clear"></i><i class="towel towel--clear"></i><i class="towel towel--clear"></i>
    </div>
    <div class="crowd-row">
      <i class="towel towel--clear"></i><i class="towel towel--clear"></i><i class="towel towel--clear"></i><i class="towel towel--clear"></i><i class="towel towel--cancer"></i><i class="towel towel--clear"></i><i class="towel towel--cancer"></i><i class="towel towel--clear"></i><i class="towel towel--clear"></i><i class="towel towel--clear"></i><i class="towel towel--clear"></i><i class="towel towel--cancer"></i><i class="towel towel--clear"></i>
    </div>
    <div class="crowd-row">
      <i class="towel towel--clear"></i><i class="towel towel--clear"></i><i class="towel towel--clear"></i><i class="towel towel--clear"></i><i class="towel towel--clear"></i><i class="towel towel--cancer"></i><i class="towel towel--clear"></i><i class="towel towel--melanoma"></i><i class="towel towel--clear"></i><i class="towel towel--clear"></i><i class="towel towel--cancer"></i><i class="towel towel--clear"></i>
    </div>
  </div>

  <svg class="shore" viewBox="0 0 1200 120" preserveAspectRatio="none" aria-hidden="true">
    <path d="M0 40 C 160 40, 260 5, 430 22 C 600 40, 700 70, 860 45 C 980 25, 1080 15, 1200 30 L1200 120 L0 120 Z" fill="#ffffff"/>
    <path d="M0 52 C 160 52, 260 18, 430 34 C 600 52, 700 82, 860 57 C 980 37, 1080 27, 1200 42 L1200 120 L0 120 Z" fill="var(--sea)"/>
  </svg>

  <aside class="legend">
    <div class="legend-item"><i class="towel towel--clear"></i><span>No skin cancer</span></div>
    <div class="legend-item"><i class="towel towel--cancer"></i><span>Skin cancer</span></div>
    <div class="legend-item"><i class="towel towel--melanoma"></i><span>Melanoma</span></div>
  </aside>
</body>
</html>
```